Business Card / Appointment Card for Physician

On one side it should give the logo, address, and contact information, and on the other side it should br an Appointment card.

One Side:
Logo (see attached files)
Board Certified American Orthopedic Surgery

1487 Harrowgate Ave.
Suite KM7
Bronx, NY 10527
Tel: (718) 552 - 1948
Fax: (718) 552 - 7210

628 Fourth Ave.
Suite 42
New York, NY 10087
Tel: (212) 734 - 2815

Second Side:
Appointment
give them a choice of Bronx or Mahattan office
For:
Date:
Time:

If you are unable to keep your appointment, please call (718) 263-5102 24hrs in advance.

Target Market(s)

People that need orthopedic surgery

Industry/Entity Type

Business

Contact Information for Business Card

smart and attractive

Requirements
Must have
• logo
• contact information on one side, appointment information on the other

```html
<!DOCTYPE html>
<html lang="en">
<head>
<meta charset="utf-8">
<title>Dana R. Whitfield MD PC – Business and Appointment Card</title>
<link href="https://fonts.googleapis.com/css2?family=Open+Sans:wght@300;400;700&family=Roboto+Condensed:wght@400&display=swap" rel="stylesheet">
<style>
  :root {
    --brand-blue: #0664a6;
    --ink-blue: #1d5d8e;
    --brand-green: #6db33f;
    --paper: #ffffff;
    --circle-soft: #e9eef4;
    --circle-soft-alt: #eef2f0;
    --rule: #9aa6b2;
  }
  html, body {
    margin: 0;
    padding: 0;
    width: 973px;
    height: 1200px;
    overflow: hidden;
    background: var(--paper);
  }
  .canvas {
    position: relative;
    width: 973px;
    height: 1200px;
    overflow: hidden;
    background: var(--paper);
    font-family: "Open Sans", sans-serif;
  }
  .card {
    position: absolute;
    left: 0;
    transform-origin: top left;
    transform: rotate(-90deg);
    overflow: hidden;
    background: var(--paper);
  }
  .card--contact { top: 620px; width: 620px; height: 973px; }
  .card--appointment { top: 1200px; width: 560px; height: 973px; }

  /* Contact side */
  .brand-dot {
    position: absolute; left: 255px; top: 14px;
    width: 105px; height: 105px; border-radius: 50%;
    background: var(--brand-green);
  }
  .brand-name {
    position: absolute; left: 55px; top: 132px; width: 510px;
    font-family: "Roboto Condensed", sans-serif; font-weight: 400;
    font-size: 38px; letter-spacing: 0.5px; color: var(--brand-blue);
    white-space: nowrap; line-height: 1;
  }
  .brand-specialty {
    position: absolute; left: 58px; top: 178px;
    font-family: "Roboto Condensed", sans-serif; font-size: 17px;
    color: var(--brand-blue); white-space: nowrap; line-height: 1;
  }
  .brand-rule {
    position: absolute; left: 58px; top: 210px; width: 490px;
    height: 1px; background: var(--rule);
  }
  .brand-tagline {
    position: absolute; left: 58px; top: 228px;
    font-size: 16px; letter-spacing: 0.6px; color: var(--brand-green);
    white-space: nowrap; line-height: 1;
  }
  .contact-panel {
    position: absolute; left: -99px; top: 263px;
    width: 818px; height: 818px; border-radius: 50%;
    background: var(--brand-blue);
  }
  .contact-line {
    position: absolute; left: 0; width: 620px; text-align: center;
    color: var(--paper); font-weight: 300; font-size: 24px;
    letter-spacing: 1px; white-space: nowrap; line-height: 1;
  }
  .contact-line--phone { font-size: 26px; }
  .contact-label { color: var(--brand-green); }
  .office-divider {
    position: absolute; left: 0; top: 660px; width: 620px;
    display: flex; justify-content: center; gap: 15px;
  }
  .office-divider span {
    width: 26px; height: 26px; border-radius: 50%; background: var(--brand-green);
  }

  /* Appointment side */
  .anatomy-panel {
    position: absolute; left: 80px; width: 440px; height: 440px; border-radius: 50%;
  }
  .anatomy-panel--knee { top: 30px; background: linear-gradient(90deg, var(--circle-soft), #e4f3fb); }
  .anatomy-panel--shoulder { top: 487px; background: linear-gradient(90deg, var(--circle-soft-alt), var(--circle-soft)); }
  .appointment-title {
    position: absolute; left: 170px; top: 30px;
    font-weight: 700; font-size: 32px; letter-spacing: 2px;
    color: var(--ink-blue); line-height: 1;
  }
  .appointment-rule {
    position: absolute; left: 200px; top: 85px; width: 200px;
    height: 1px; background: var(--brand-blue);
  }
  .office-choice {
    position: absolute; left: 115px;
    font-weight: 300; font-size: 26px; letter-spacing: 1px;
    color: var(--ink-blue); white-space: nowrap; line-height: 1;
    display: flex; align-items: center; gap: 6px;
  }
  .office-choice::before {
    content: ""; width: 19px; height: 19px;
    border: 2px solid var(--ink-blue); border-radius: 50%;
  }
  .field-label {
    position: absolute; left: 80px;
    font-weight: 300; font-size: 26px; letter-spacing: 1px;
    color: var(--ink-blue); line-height: 1;
  }
  .cancellation-note {
    position: absolute; left: 40px; top: 768px; width: 520px;
    text-align: center; font-weight: 300; font-size: 27px;
    letter-spacing: 1px; line-height: 45px; color: var(--ink-blue);
    margin: 0;
  }
  .cancellation-note .phone { color: var(--brand-green); }
</style>
</head>
<body>
<main class="canvas">

  <section class="card card--contact" aria-label="Contact side">
    <div class="brand-dot"></div>
    <div class="brand-name">DANA R. WHITFIELD MD PC</div>
    <div class="brand-specialty">ORTHOPAEDIC SURGERY &amp; SPORTS MEDICINE</div>
    <div class="brand-rule"></div>
    <div class="brand-tagline">BOARD CERTIFIED AMERICAN ORTHOPEDIC SURGERY</div>

    <div class="contact-panel"></div>

    <div class="contact-line" style="top:455px">1487 HARROWGATE AVE. SUITE KM7</div>
    <div class="contact-line" style="top:505px">BRONX, NY 10527</div>
    <div class="contact-line contact-line--phone" style="top:551px"><span class="contact-label">Tel:</span> (718) 552 - 1948</div>
    <div class="contact-line contact-line--phone" style="top:591px"><span class="contact-label">Fax:</span> (718) 552 - 7210</div>

    <div class="office-divider"><span></span><span></span><span></span><span></span></div>

    <div class="contact-line" style="top:733px">628 FOURTH AVE. SUITE 42</div>
    <div class="contact-line" style="top:783px">NEW YORK, NY 10087</div>
    <div class="contact-line contact-line--phone" style="top:831px"><span class="contact-label">Tel:</span> (212) 734 - 2815</div>
  </section>

  <section class="card card--appointment" aria-label="Appointment side">
    <div class="anatomy-panel anatomy-panel--knee" role="img" aria-label="Faint line illustration of a knee joint"></div>
    <div class="anatomy-panel anatomy-panel--shoulder" role="img" aria-label="Faint line illustration of a shoulder joint"></div>

    <div class="appointment-title">APPOINTMENT</div>
    <div class="appointment-rule"></div>

    <div class="office-choice" style="top:145px">BRONX OFFICE</div>
    <div class="office-choice" style="top:215px">MANHATTAN OFFICE</div>

    <div class="field-label" style="top:343px">FOR:</div>
    <div class="field-label" style="top:460px">DATE:</div>
    <div class="field-label" style="top:577px">TIME:</div>

    <p class="cancellation-note">IF YOU ARE UNABLE TO<br>KEEP YOUR APPOINTMENT<br>PLEASE CALL <span class="phone">(718) 263-5102</span><br>24HRS IN ADVANCE</p>
  </section>

</main>
</body>
</html>
```